fernbrook stationary
cards + stationary
Professional
owen hale
director
52 pelham row
Ashcombe
herts
wd7 2lr
owen@fernbrookltd.co.uk
www.fernbrookltd.co.uk
require letter heading + comp slips
'retail and commercial solutions'
+ logo
font is 'goodtimes'

```html
<!DOCTYPE html>
<html lang="en">
<head>
<meta charset="utf-8">
<title>Fernbrook Stationery</title>
<link href="https://fonts.googleapis.com/css2?family=Open+Sans:wght@300;400;600;700&display=swap" rel="stylesheet">
<style>
  :root {
    --bg: #d9dcdf;
    --paper: #ffffff;
    --blue-deep: #0a3f9e;
    --blue: #1a63d0;
    --blue-light: #5ea3ef;
    --accent: #d42a2a;
    --ink: #3b3b3b;
    --muted: #8a8f96;
    --ghost: #eceef1;
  }
  * { box-sizing: border-box; margin: 0; padding: 0; }
  html, body { width: 1200px; height: 871px; overflow: hidden; }
  body {
    background: var(--bg);
    position: relative;
    font-family: "Open Sans", Arial, sans-serif;
    color: var(--ink);
  }
  .sheet { position: absolute; background: var(--paper); box-shadow: 0 4px 14px rgba(0,0,0,.18); overflow: hidden; }
  .sheet svg.waves { position: absolute; inset: 0; width: 100%; height: 100%; }
  .brand {
    position: absolute; display: flex; align-items: center; gap: 6px;
    font-family: "Open Sans", Arial, sans-serif; font-weight: 700;
    color: var(--blue-deep); white-space: nowrap;
  }
  .brand .dot { border-radius: 50%; background: var(--blue); flex: none; }
  .ghost-name {
    position: absolute; font-family: "Open Sans", Arial, sans-serif; font-weight: 300;
    color: var(--ghost); white-space: nowrap;
  }
  .address { position: absolute; font-size: 8px; line-height: 1.55; color: var(--ink); }
  .address .label { color: var(--blue); font-weight: 700; margin-right: 3px; }
  .address .web { color: var(--blue); font-weight: 700; }

  /* Letterhead */
  .letterhead { left: 53px; top: 29px; width: 494px; height: 715px; }
  .letterhead .brand { left: 26px; top: 34px; font-size: 22px; }
  .letterhead .brand .dot { width: 10px; height: 10px; }
  .letterhead .address { left: 384px; top: 108px; width: 100px; }
  .letterhead .ghost-name { left: 36px; top: 430px; font-size: 62px; }
  .letterhead .footer { position: absolute; left: 0; right: 0; bottom: 16px; text-align: center; font-size: 6px; color: var(--muted); }

  /* Business card front */
  .card-front { left: 607px; top: 204px; width: 204px; height: 132px; border-radius: 8px; }
  .card-front .brand { left: 10px; top: 10px; font-size: 12px; }
  .card-front .brand .dot { width: 6px; height: 6px; }
  .card-front .person { position: absolute; left: 12px; top: 64px; }
  .card-front .name { font-size: 8px; font-weight: 700; color: var(--accent); text-transform: uppercase; letter-spacing: .04em; }
  .card-front .role { font-size: 6.5px; color: var(--ink); }
  .card-front .contact { position: absolute; left: 12px; top: 88px; font-size: 6px; line-height: 1.5; }
  .card-front .contact .label { color: var(--blue); font-weight: 700; margin-right: 3px; }
  .card-front .side-address { position: absolute; left: 134px; top: 48px; font-size: 6px; line-height: 1.5; width: 66px; }

  /* Business card back */
  .card-back {
    left: 830px; top: 204px; width: 231px; height: 132px; border-radius: 8px;
    background: radial-gradient(ellipse at 45% 45%, var(--blue-light) 0%, var(--blue) 45%, var(--blue-deep) 100%);
  }
  .card-back .tagline { position: absolute; left: 0; right: 0; top: 18px; text-align: center; font-size: 6.5px; font-weight: 600; color: #fff; letter-spacing: .12em; text-transform: uppercase; }
  .card-back .brand { left: 50%; top: 54px; transform: translateX(-50%); font-size: 17px; color: #fff; }
  .card-back .brand .dot { width: 8px; height: 8px; background: #fff; }
  .card-back .web { position: absolute; left: 0; right: 0; bottom: 16px; text-align: center; font-size: 6.5px; font-weight: 600; color: #fff; }

  /* Envelope */
  .envelope { left: 540px; top: 444px; width: 612px; height: 384px; }
  .envelope .return-note { position: absolute; left: 110px; top: 22px; font-size: 6px; color: #fff; letter-spacing: .05em; text-transform: uppercase; }
  .envelope .brand { left: 28px; top: 200px; font-size: 20px; }
  .envelope .brand .dot { width: 9px; height: 9px; }
  .envelope .ghost-name { right: 22px; top: 236px; font-size: 42px; }
  .envelope .address { left: 512px; top: 300px; width: 90px; font-size: 7px; }
</style>
</head>
<body>

<section class="sheet letterhead" aria-label="Letterhead">
  <svg class="waves" viewBox="0 0 494 715" preserveAspectRatio="none" aria-hidden="true">
    <defs>
      <linearGradient id="lh-band" x1="0" x2="1" y1="0" y2="0">
        <stop offset="0" stop-color="#5ea3ef"/>
        <stop offset=".5" stop-color="#1a63d0"/>
        <stop offset="1" stop-color="#0a3f9e"/>
      </linearGradient>
    </defs>
    <path d="M0,78 C150,130 320,60 494,12 L494,26 C320,76 150,150 0,98 Z" fill="url(#lh-band)"/>
    <path d="M0,70 C160,118 330,50 494,6" stroke="#5ea3ef" stroke-width="1.5" fill="none"/>
    <path d="M0,104 C160,155 330,82 494,32" stroke="#9cc6f5" stroke-width="1" fill="none"/>
  </svg>
  <div class="brand"><span class="dot"></span>FERNBROOK</div>
  <div class="address">
    52 Pelham Row<br>Ashcombe<br>Hartshire<br>WD7 2LR<br>
    <span class="label">(t)</span>01632 960 014<br>
    <span class="web">www.fernbrookltd.co.uk</span>
  </div>
  <div class="ghost-name">FERNBROOK</div>
  <div class="footer">Company Registration No. 0000000 &nbsp;|&nbsp; VAT Reg No. 000 0000 00 &nbsp;|&nbsp; Registered in England &nbsp;|&nbsp; Ashcombe</div>
</section>

<section class="sheet card-front" aria-label="Business card front">
  <svg class="waves" viewBox="0 0 204 132" preserveAspectRatio="none" aria-hidden="true">
    <path d="M0,42 C60,62 130,36 204,16 L204,23 C130,44 60,72 0,50 Z" fill="#1a63d0"/>
    <path d="M0,38 C60,56 130,30 204,11" stroke="#5ea3ef" stroke-width="1" fill="none"/>
  </svg>
  <div class="brand"><span class="dot"></span>FERNBROOK</div>
  <div class="side-address">52 Pelham Row<br>Ashcombe<br>Hartshire, WD7 2LR</div>
  <div class="person">
    <div class="name">Owen Hale</div>
    <div class="role">Director</div>
  </div>
  <div class="contact">
    <span class="label">(m)</span>07700 900 321<br>
    <span class="label">(e)</span>owen@fernbrookltd.co.uk<br>
    <span class="label">(w)</span>www.fernbrookltd.co.uk
  </div>
</section>

<section class="sheet card-back" aria-label="Business card back">
  <div class="tagline">Retail and Commercial Solutions</div>
  <div class="brand"><span class="dot"></span>FERNBROOK</div>
  <div class="web">www.fernbrookltd.co.uk</div>
</section>

<section class="sheet envelope" aria-label="Envelope">
  <svg class="waves" viewBox="0 0 612 384" preserveAspectRatio="none" aria-hidden="true">
    <defs>
      <linearGradient id="env-fill" x1="0" x2="0" y1="0" y2="1">
        <stop offset="0" stop-color="#0a3f9e"/>
        <stop offset=".6" stop-color="#1a63d0"/>
        <stop offset="1" stop-color="#5ea3ef"/>
      </linearGradient>
    </defs>
    <path d="M0,0 H612 V100 C440,130 250,215 0,175 Z" fill="url(#env-fill)"/>
    <path d="M0,183 C250,225 440,140 612,110" stroke="#1a63d0" stroke-width="5" fill="none"/>
    <path d="M0,192 C250,235 440,152 612,122" stroke="#9cc6f5" stroke-width="1.2" fill="none"/>
  </svg>
  <div class="return-note">If undelivered please return</div>
  <div class="brand"><span class="dot"></span>FERNBROOK</div>
  <div class="ghost-name">FERNBROOK</div>
  <div class="address">
    52 Pelham Row<br>Ashcombe<br>Hartshire, WD7 2LR<br>
    <span class="label">(t)</span>01632 960 014<br>
    <span class="web">www.fernbrookltd.co.uk</span>
  </div>
</section>

</body>
</html>
```